Storm Restoration Contractor needs a professional letterhead design

Looking for a professional letterhead design. Not looking for your cheapo MS Word standard ones that are readily available. Dont want it to be cookie cutter look like ones readily available online. We just recently changed our logo and want to freshen up all our documents. Our company handles restoring a property back to a pre-loss condition after a storm damages it. For example, wind, hail, flood, fire losses.

Target Market(s)

Property Owners, Homeowners, Property Owners, Commercial Property Owners, Property Management Companies

Industry/Entity Type

Construction Company

Requirements
Must have
• Professional, Use 1 of 2 logo options
• Storm Restoration, Roofing, Siding, Windows

```html
<!DOCTYPE html>
<html lang="en">
<head>
<meta charset="utf-8">
<title>Kestrel Exteriors Letterhead</title>
<link href="https://fonts.googleapis.com/css2?family=Open+Sans:wght@400;600;700&display=swap" rel="stylesheet">
<style>
  :root {
    --brand-blue: #1472b9;
    --ink: #3a3a3a;
    --ink-soft: #555b61;
    --paper: #ffffff;
    --backdrop: #e8e9ea;
    --curve-grey: #d9dadb;
  }
  * { box-sizing: border-box; margin: 0; padding: 0; }
  html, body {
    width: 1200px; height: 720px; overflow: hidden;
    background: var(--backdrop);
    font-family: "Open Sans", Arial, sans-serif;
  }
  .canvas {
    position: relative; width: 1200px; height: 720px;
    display: flex; justify-content: center; align-items: center; gap: 40px;
  }
  .sheet {
    position: relative; width: 453px; height: 640px;
    box-shadow: 0 6px 18px rgba(0,0,0,0.12);
    overflow: hidden;
  }
  .letterhead { background: var(--paper); color: var(--ink); }
  .letterhead__header {
    position: absolute; top: 40px; left: 40px; right: 36px;
    display: flex; justify-content: space-between; align-items: flex-start;
  }
  .brand {
    display: flex; align-items: center; gap: 8px;
    color: var(--brand-blue); font-weight: 700;
    font-size: 17px; letter-spacing: 0.5px; line-height: 1; text-transform: uppercase;
  }
  .brand__dot {
    width: 22px; height: 22px; border-radius: 50%; background: var(--brand-blue);
  }
  .contact {
    font-size: 6.5px; line-height: 1.45; color: var(--ink-soft); font-weight: 600;
  }
  .contact__address { margin-bottom: 5px; }
  .contact__row { display: flex; align-items: center; gap: 4px; }
  .contact__row svg { width: 6px; height: 6px; fill: var(--brand-blue); }
  .letter {
    position: absolute; top: 128px; left: 40px; right: 40px;
    font-size: 7.4px; line-height: 1.4; color: var(--ink-soft);
  }
  .letter__recipient { margin-bottom: 10px; }
  .letter p { margin-bottom: 9px; }
  .letter__sign { margin-top: 34px; }
  .letterhead__footer {
    position: absolute; left: 0; bottom: 0; width: 453px; height: 110px;
  }
  .cover {
    background: var(--brand-blue);
    display: flex; justify-content: center; align-items: center;
  }
  .cover .brand {
    color: var(--paper); font-size: 22px; letter-spacing: 1px;
  }
  .cover .brand__dot { background: var(--paper); width: 28px; height: 28px; }
</style>
</head>
<body>
<main class="canvas">
  <section class="sheet letterhead">
    <header class="letterhead__header">
      <div class="brand"><span class="brand__dot"></span>Kestrel Exteriors</div>
      <address class="contact">
        <div class="contact__address">512 Harbor Ridge Rd Ste 210,<br>Lakemont, MD 20911</div>
        <div class="contact__row"><svg viewBox="0 0 10 10"><path d="M2 0l2 2-1 2c1 1 2 2 3 3l2-1 2 2-2 2C4 10 0 6 0 2z"/></svg>555-014-2290</div>
        <div class="contact__row"><svg viewBox="0 0 10 10"><rect x="0" y="2" width="10" height="6" rx="1"/></svg>555-014-2291</div>
        <div class="contact__row"><svg viewBox="0 0 10 10"><circle cx="5" cy="5" r="5"/></svg>www.kestrelexteriors.com</div>
      </address>
    </header>

    <article class="letter">
      <div class="letter__recipient">
        Mr. Daniel Reyes<br>Managing Director<br>Northfield Holdings<br>240 Cedar Lane<br>USA
      </div>
      <p>Lorem ipsum dolor sit amet, consectetuer adipiscing elit. Nam cursus. Morbi ut mi. Nullam enim leo, egestas id, condimentum at, laoreet mattis, massa. Sed eleifend nonummy diam. Praesent mauris ante, elementum et, bibendum at, posuere sit amet, nibh. Duis tincidunt lectus quis dui viverra vestibulum.</p>
      <p>Suspendisse vulputate aliquam dui. Nulla elementum dui ut augue. Aliquam vehicula mi at mauris. Maecenas placerat, nisl at consequat rhoncus, sem nunc gravida justo, quis eleifend arcu velit quis lacus. Morbi magna magna, tincidunt a, mattis non, imperdiet vitae, tellus. Sed odio est, auctor ac, sollicitudin in, consequat vitae, orci. Fusce id felis. Vivamus sollicitudin.</p>
      <p>Metus eget eros. Pellentesque habitant morbi tristique senectus et netus et malesuada fames ac turpis egestas. In posuere felis nec tortor. Pellentesque faucibus. Ut accumsan ultricies elit. Maecenas at justo id velit placerat molestie. Donec dictum lectus non odio. Cras a ante vitae enim iaculis aliquam.</p>
      <p>Mauris nunc quam, venenatis nec, euismod sit amet, egestas placerat, est. Pellentesque habitant morbi tristique senectus et netus et malesuada fames ac turpis egestas. Cras id elit. Integer quis urna. Ut ante enim, dapibus malesuada, fringilla eu, condimentum quis, tellus. Aenean porttitor eros vel dolor. Donec convallis pede venenatis nibh. Duis quam. Nam eget.</p>
      <p>Thank you for being one of our valued customers.</p>
      <div class="letter__sign">Name Here<br>CEO</div>
    </article>

    <svg class="letterhead__footer" viewBox="0 0 453 110" preserveAspectRatio="none" aria-hidden="true">
      <path d="M0 0 C60 60 200 80 453 82 L453 110 L0 110 Z" fill="var(--curve-grey)"/>
      <path d="M120 78 C250 92 360 88 453 70 L453 110 L0 110 L0 104 C40 90 80 82 120 78 Z" fill="var(--brand-blue)"/>
      <path d="M0 108 C120 98 300 100 453 92 L453 110 L0 110 Z" fill="var(--curve-grey)"/>
    </svg>
  </section>

  <section class="sheet cover">
    <div class="brand"><span class="brand__dot"></span>Kestrel Exteriors</div>
  </section>
</main>
</body>
</html>
```